Business Card design for construction company

I would like a business card design for a construction company - Harlow Constructions. I have attached the ai logo file for use. I would like the card to be very smart and clean and incorporate only white and the two colours in the logo. I would like the card to have two sides. One side can just have the logo, the other with the relevant information.

Target Market(s)

Building and Construction Clients

Industry/Entity Type

Business

Contact Information for Business Card

Name: Tom Pardoe
Company: Harlow Constructions Pty Limited
Address: 14 Mallee Crescent Carrow Vale 2093
Phone: 0427 531 068
Email: tomp@harlowbuild-example.com.au

Font styles to use
Serif
Sans Serif

Requirements
Must have
• Details noted above
• Logo as provided
• Colours as in logo
• Square edges
• A font that compliments the logo
Should not have
• Any colour other than white and those in logo
• Rounded edges

```html
<!DOCTYPE html>
<html lang="en">
<head>
<meta charset="utf-8">
<title>Harlow Constructions – Business Card</title>
<link rel="stylesheet" href="https://fonts.googleapis.com/css2?family=Michroma&family=Montserrat:wght@300;400&display=swap">
<style>
  :root {
    --stage: #141414;
    --slate: #5b5c5e;
    --slate-dark: #48494b;
    --slate-light: #6c6d70;
    --paper: #ffffff;
    --paper-shade: #eeeeee;
    --ink: #5a5b5e;
    --ink-soft: #6e6f72;
    --accent: #29abe2;
  }
  * { box-sizing: border-box; margin: 0; padding: 0; }
  html, body {
    width: 1200px; height: 864px; overflow: hidden;
    background: var(--stage);
  }
  .stage {
    position: relative; width: 1200px; height: 864px;
    display: flex; align-items: center; justify-content: center; gap: 48px;
  }
  .card {
    position: relative; width: 520px; height: 318px; overflow: hidden;
  }

  /* Front: contact side */
  .card--front {
    background: linear-gradient(160deg, var(--paper) 55%, var(--paper-shade));
  }
  .side-band {
    position: absolute; left: 0; top: 0; bottom: 0; width: 96px;
    background: linear-gradient(180deg, var(--slate-light), var(--slate));
  }
  .accent-rule-v {
    position: absolute; top: 0; bottom: 0; right: 40px; width: 2px;
    background: var(--accent);
  }
  .accent-rule-h {
    position: absolute; left: 60px; top: 112px; width: 72px; height: 2px;
    background: var(--accent);
  }
  .brand {
    position: absolute; right: 66px; top: 52px;
    font-family: "Michroma", sans-serif; font-size: 15px; letter-spacing: 2px;
    color: var(--ink); text-transform: uppercase;
  }
  .holder-name {
    position: absolute; left: 124px; top: 116px;
    font-family: "Michroma", sans-serif; font-size: 13px; letter-spacing: 2px;
    color: var(--ink); text-transform: uppercase;
  }
  .contact-list {
    position: absolute; left: 124px; top: 150px; list-style: none;
    font-family: "Montserrat", sans-serif; font-weight: 300; font-size: 13px;
    line-height: 19px; color: var(--ink-soft); font-style: italic;
  }
  .contact-icons {
    position: absolute; left: 68px; top: 150px;
    display: flex; flex-direction: column; gap: 5px;
  }
  .contact-icons svg { display: block; }
  .legal-name {
    position: absolute; right: 66px; bottom: 30px;
    font-family: "Montserrat", sans-serif; font-weight: 300; font-style: italic;
    font-size: 13px; color: var(--ink-soft);
  }

  /* Back: brand side */
  .card--back {
    background: linear-gradient(150deg, var(--slate-light) 0%, var(--slate) 50%, var(--slate-dark) 100%);
  }
  .back-rule {
    position: absolute; left: 150px; right: 0; top: 176px; height: 2px;
    background: var(--accent);
  }
  .back-brand {
    position: absolute; right: 40px; top: 108px; text-align: right;
    font-family: "Michroma", sans-serif; color: var(--paper);
    text-transform: uppercase; line-height: 1.15;
  }
  .back-brand .line-1 { display: block; font-size: 44px; letter-spacing: 4px; }
  .back-brand .line-2 { display: block; font-size: 16px; letter-spacing: 4px; margin-top: 22px; }
</style>
</head>
<body>
<main class="stage">
  <section class="card card--front" aria-label="Business card, contact side">
    <div class="side-band"></div>
    <div class="accent-rule-h"></div>
    <div class="accent-rule-v"></div>
    <div class="brand">Harlow Constructions</div>
    <h1 class="holder-name">Tom Pardoe</h1>
    <div class="contact-icons" aria-hidden="true">
      <svg width="14" height="14" viewBox="0 0 14 14"><circle cx="7" cy="7" r="7" fill="var(--accent)"/><path d="M4.6 3.8l1.3 1.2-.6 1c.5 1 1.2 1.7 2.2 2.2l1-.6 1.2 1.3-.8.9C6.8 9.6 4.4 7.2 4.1 4.6z" fill="#fff"/></svg>
      <svg width="14" height="14" viewBox="0 0 14 14"><circle cx="7" cy="7" r="7" fill="var(--accent)"/><rect x="3.6" y="4.6" width="6.8" height="4.8" fill="none" stroke="#fff" stroke-width="1"/><path d="M3.8 4.8L7 7.4l3.2-2.6" fill="none" stroke="#fff" stroke-width="1"/></svg>
      <svg width="14" height="14" viewBox="0 0 14 14"><circle cx="7" cy="7" r="7" fill="var(--accent)"/><path d="M7 3.2a2.4 2.4 0 0 1 2.4 2.4C9.4 7.4 7 10.6 7 10.6S4.6 7.4 4.6 5.6A2.4 2.4 0 0 1 7 3.2z" fill="#fff"/><circle cx="7" cy="5.6" r=".9" fill="var(--accent)"/></svg>
    </div>
    <ul class="contact-list">
      <li>0427 531 068</li>
      <li>tomp@harlowbuild-example.com.au</li>
      <li>14 Mallee Crescent Carrow Vale 2093</li>
    </ul>
    <p class="legal-name">Harlow Constructions Pty Limited</p>
  </section>

  <section class="card card--back" aria-label="Business card, brand side">
    <div class="back-rule"></div>
    <div class="back-brand">
      <span class="line-1">Harlow</span>
      <span class="line-2">Constructions</span>
    </div>
  </section>
</main>
</body>
</html>
```